Website Design for PawRank - New Digital Agency

We are creating a new digital marketing agency and need a new website. I have attached the logo. Our niche is going to be veterinarians. Use the same colors as in the logo (blue, white and gray).

I want real pictures of real people in this and not just boring stock photos. It needs to be related to the industry.

Home page (example:https://trellmarsh.com/)
Service page (example: https://dovequist.com/consulting/)
Case study page (example: https://www.harlowfinchley.com/seo/case-study/)

I will continue to update this brief.
Updates

I updated the brief with some additional sample sites 2 days ago and want to see more designs. I won't need that may more days ...just a few more.

Target Market(s)

veterinarians

Font styles to use
Sans Serif

Requirements
Must have
• I want a very clean looking site. Use the same colors as in the logo (blue, white and gray).
Nice to have
• We need to build this with the idea that the purpose is to generate leads for our business.
• Home page (example:https://trellmarsh.com/)
• Service page (example: https://dovequist.com/consulting/)
• Case study page (example: https://www.harlowfinchley.com/seo/case-study/)

```html
<!DOCTYPE html>
<html lang="en">
<head>
<meta charset="utf-8">
<title>PawRank – Digital Marketing for Veterinarians</title>
<link href="https://fonts.googleapis.com/css2?family=Arimo:wght@400;700&display=swap" rel="stylesheet">
<style>
:root{
  --blue:#1663c2;
  --blue-dark:#0f56ad;
  --page:#e8e8e8;
  --white:#ffffff;
  --ink:#555555;
  --ink-soft:#6a6a6a;
  --footer:#232127;
  --field:#55545a;
}
*{box-sizing:border-box;margin:0;padding:0}
html,body{width:1200px;height:3177px;overflow:hidden}
body{position:relative;background:var(--white);font-family:"Arimo",Arial,sans-serif;color:var(--ink)}
.page{position:absolute;left:0;top:0;width:1200px;height:3117px;background:var(--page)}
.abs{position:absolute}

/* hero */
.hero-photo{left:0;top:0;width:1200px;height:580px;
  background:linear-gradient(100deg,#b9b7b2 0%,#cfcbc3 30%,#c8b79a 50%,#9a9a8f 72%,#6f8a55 100%)}
.nav-bar{left:0;top:0;width:1200px;height:84px;background:rgba(120,140,170,.35)}
.logo{left:28px;top:24px;display:flex;align-items:center;gap:8px;font-size:36px;font-weight:700;color:var(--blue)}
.logo-dot{width:26px;height:26px;border-radius:50%;background:var(--blue)}
.nav{left:392px;top:43px;display:flex;gap:0;font-size:18px;font-weight:700;color:var(--white)}
.nav span{position:absolute;white-space:nowrap}
.search{left:965px;top:42px}
.social{top:36px;width:24px;height:24px;border-radius:50%;background:#2a6fd0}
.hero-title{left:0;top:160px;width:1204px;text-align:center;font-size:56px;line-height:64px;font-weight:700;color:var(--white)}
.quote-form{left:397px;top:425px;width:398px;height:52px;border-radius:26px;background:var(--white)}
.quote-form .email{position:absolute;left:74px;top:17px;font-size:17px;color:#aaa}
.quote-form .btn{position:absolute;left:248px;top:5px;width:145px;height:42px;border-radius:21px;background:var(--blue);color:var(--white);font-size:16px;text-align:center;line-height:42px}
.intro-boxes{left:197px;top:503px;width:806px;height:127px;display:flex;border:2px solid #bcc9dc;background:#bcc9dc;gap:3px}
.intro-box{flex:1;background:var(--blue);color:var(--white);padding:18px 30px 0;text-align:center}
.intro-box h3{font-size:15px;font-weight:700;margin-bottom:18px}
.intro-box p{font-size:13.5px;line-height:17px;text-align:left}

/* about */
.video{left:221px;top:734px;width:385px;height:327px;border:3px solid var(--white);box-shadow:0 2px 6px rgba(0,0,0,.25);
  background:linear-gradient(120deg,#f1f1ef 0%,#e3e6e2 40%,#cbd2d6 100%)}
.play{left:384px;top:873px}
.about-title{left:640px;top:722px;width:360px;font-size:33px;line-height:38px;font-weight:700;color:var(--ink)}
.about-text{left:643px;width:300px;font-size:13.5px;line-height:16.5px;color:var(--ink-soft)}
.read-more{left:647px;top:1042px;width:109px;height:22px;border-radius:11px;background:var(--blue);color:var(--white);font-size:12px;font-weight:700;text-align:center;line-height:22px}

/* bands */
.band{left:0;width:1200px;background:var(--blue);color:var(--white);text-align:center}
.band-title{font-size:32px;font-weight:700}
.lead{left:0;width:1200px;text-align:center;font-size:17px;line-height:21px;color:var(--ink-soft)}

/* services */
.card{background:var(--white);box-shadow:0 1px 4px rgba(0,0,0,.18);text-align:center;padding:0 18px}
.card h3{font-size:24px;font-weight:700;color:var(--ink);margin-top:56px;margin-bottom:16px}
.card p{font-size:12.5px;line-height:15px;color:var(--ink-soft)}

/* stats */
.stat{top:1903px;width:300px;text-align:center;color:var(--white);font-size:23px;line-height:36px}

/* testimonials */
.quote-card{top:2285px;width:380px;height:201px;background:var(--white);border-radius:16px 16px 16px 16px;box-shadow:0 1px 4px rgba(0,0,0,.2);padding:44px 26px 0;font-size:15px;line-height:19px;color:var(--ink-soft)}
.avatar{top:2491px}
.client-name{top:2516px;font-size:21px;color:var(--ink-soft)}

/* cta + footer */
.footer{left:0;top:2769px;width:1200px;height:348px;background:var(--footer)}
.cta-shape{left:196px;top:2701px}
.cta-title{left:228px;top:2727px;font-size:32px;font-weight:700;color:var(--white)}
.cta-text{left:230px;top:2772px;font-size:12.5px;line-height:15px;color:var(--white)}
.cta-btn{left:799px;top:2742px;width:151px;height:28px;border-radius:14px;background:var(--white);color:var(--blue);font-size:13px;font-weight:700;text-align:center;line-height:28px}
.col-title{top:2904px;font-size:16px;color:var(--white)}
.col-rule{top:2931px;width:74px;height:3px;background:var(--blue)}
.col-text{top:2960px;font-size:13.5px;line-height:17px;color:var(--white)}
.col-list{list-style:none;font-size:12px;line-height:17.5px;color:var(--white)}
.col-list li::before{content:"";display:inline-block;width:7px;height:7px;border-radius:50%;background:var(--white);margin-right:6px;vertical-align:1px}
.field{height:29px;border-radius:7px;background:var(--field);color:var(--white);font-size:11px;text-align:center;line-height:29px}
.send{background:var(--blue);font-weight:700;font-size:10px}
</style>
</head>
<body>
<div class="page">

  <!-- hero -->
  <div class="abs hero-photo" role="img" aria-label="Smiling veterinarian with stethoscope examining a golden retriever puppy in a bright clinic"></div>
  <div class="abs nav-bar"></div>
  <div class="abs logo"><span>PawRank</span><span class="logo-dot"></span></div>
  <nav class="abs nav" style="left:0;top:43px">
    <span style="left:392px">Home</span>
    <span style="left:480px">About</span>
    <span style="left:561px">Services</span>
    <span style="left:666px">Case Study</span>
    <span style="left:799px">Blog</span>
    <span style="left:869px">Contact</span>
  </nav>
  <svg class="abs search" width="24" height="24" viewBox="0 0 24 24" aria-label="Search">
    <circle cx="12" cy="12" r="11" fill="#ffffff"/>
    <circle cx="10.5" cy="10.5" r="4" fill="none" stroke="#333" stroke-width="2"/>
    <line x1="13.5" y1="13.5" x2="17" y2="17" stroke="#333" stroke-width="2.4" stroke-linecap="round"/>
  </svg>
  <div class="abs social" style="left:1063px"></div>
  <div class="abs social" style="left:1098px"></div>
  <div class="abs social" style="left:1135px"></div>

  <h1 class="abs hero-title">WE HELP YOU GROW YOUR<br>PRACTICE FASTER</h1>
  <div class="abs quote-form">
    <span class="email">Email Address</span>
    <span class="btn">Get a Free Quote</span>
  </div>
  <div class="abs intro-boxes">
    <div class="intro-box"><h3>WHO WE ARE?</h3><p>Lorem ipsum dolor sit amet, consectetur adipiscing elit, sed do eiusmod tempor incididunt ut</p></div>
    <div class="intro-box"><h3>WHAT WE DO?</h3><p>Lorem ipsum dolor sit amet, consectetur adipiscing elit, sed do eiusmod tempor incididunt ut</p></div>
    <div class="intro-box"><h3>WHAT WE OFFER?</h3><p>Lorem ipsum dolor sit amet, consectetur adipiscing elit, sed do eiusmod tempor incididunt ut</p></div>
  </div>

  <!-- about -->
  <div class="abs video" role="img" aria-label="Video still of a veterinarian listening to a grey and white cat with a stethoscope"></div>
  <svg class="abs play" width="60" height="60" viewBox="0 0 60 60" aria-label="Play video">
    <circle cx="30" cy="30" r="29" fill="#1663c2" opacity=".9"/>
    <polygon points="24,19 24,41 42,30" fill="#ffffff"/>
  </svg>
  <h2 class="abs about-title">Lorem ipsum dolor sit amet, consectetur</h2>
  <p class="abs about-text" style="top:812px">Lorem ipsum dolor sit amet, consectetur adipiscing elit, sed do eiusmod tempor incididunt ut labore et dolore magna aliqua. Quis ipsum suspendisse ultrices gravida. Risus commodo viverra maecenas accumsan lacus vel facilisis.</p>
  <p class="abs about-text" style="top:922px">Lorem ipsum dolor sit amet, consectetur adipiscing elit, sed do eiusmod tempor incididunt ut labore et dolore magna aliqua. Quis ipsum suspendisse ultrices gravida. Risus commodo viverra maecenas accumsan lacus vel facilisis.</p>
  <div class="abs read-more">READ MORE</div>

  <!-- services -->
  <div class="abs band" style="top:1104px;height:111px;line-height:111px"><h2 class="band-title">Our Services</h2></div>
  <p class="abs lead" style="top:1252px">Lorem ipsum dolor sit amet, consectetur adipiscing<br>elit, sed do eiusmod tempor incididunt ut labore</p>

  <div class="abs card" style="left:195px;top:1348px;width:254px;height:222px"><h3>Lorem Ipsum</h3><p>Lorem ipsum dolor sit amet, consectetur adipiscing elit, sed do eiusmod tempor incididunt ut labore et dolore magna aliqua. Quis ipsum suspendisse ultrices gravida. Risus commodo viverra maecenas accumsan lacus vel facilisis.</p></div>
  <div class="abs card" style="left:474px;top:1348px;width:252px;height:222px"><h3>Lorem Ipsum</h3><p>Lorem ipsum dolor sit amet, consectetur adipiscing elit, sed do eiusmod tempor incididunt ut labore et dolore magna aliqua. Quis ipsum suspendisse ultrices gravida. Risus commodo viverra maecenas accumsan lacus vel facilisis.</p></div>
  <div class="abs card" style="left:751px;top:1348px;width:254px;height:222px"><h3>Lorem Ipsum</h3><p>Lorem ipsum dolor sit amet, consectetur adipiscing elit, sed do eiusmod tempor incididunt ut labore et dolore magna aliqua. Quis ipsum suspendisse ultrices gravida. Risus commodo viverra maecenas accumsan lacus vel facilisis.</p></div>
  <div class="abs card" style="left:195px;top:1591px;width:254px;height:222px"><h3>Lorem Ipsum</h3><p>Lorem ipsum dolor sit amet, consectetur adipiscing elit, sed do eiusmod tempor incididunt ut labore et dolore magna aliqua. Quis ipsum suspendisse ultrices gravida. Risus commodo viverra maecenas accumsan lacus vel facilisis.</p></div>
  <div class="abs card" style="left:474px;top:1591px;width:254px;height:222px"><h3>Lorem Ipsum</h3><p>Lorem ipsum dolor sit amet, consectetur adipiscing elit, sed do eiusmod tempor incididunt ut labore et dolore magna aliqua. Quis ipsum suspendisse ultrices gravida. Risus commodo viverra maecenas accumsan lacus vel facilisis.</p></div>
  <div class="abs card" style="left:751px;top:1591px;width:254px;height:222px"><h3>Lorem Ipsum</h3><p>Lorem ipsum dolor sit amet, consectetur adipiscing elit, sed do eiusmod tempor incididunt ut labore et dolore magna aliqua. Quis ipsum suspendisse ultrices gravida. Risus commodo viverra maecenas accumsan lacus vel facilisis.</p></div>

  <!-- stats -->
  <div class="abs band" style="top:1876px;height:112px"></div>
  <div class="abs stat" style="left:188px">5<br>YEARS OF EXPERIENCE</div>
  <div class="abs stat" style="left:449px">100+<br>HAPPY CLIENTS</div>
  <div class="abs stat" style="left:718px">150+<br>PROJECTS COMPLETED</div>

  <!-- testimonials -->
  <div class="abs band" style="left:196px;top:2055px;width:809px;height:107px;line-height:107px"><h2 class="band-title">What Our Clients Say?</h2></div>
  <p class="abs lead" style="top:2204px">Lorem ipsum dolor sit amet, consectetur adipiscing<br>elit, sed do eiusmod tempor incididunt ut labore</p>

  <div class="abs quote-card" style="left:196px">Lorem ipsum dolor sit amet, consectetur adipiscing elit, sed do eiusmod tempor incididunt ut labore et dolore magna aliqua. Quis ipsum suspendisse ultrices gravida. Risus commodo viverra maecenas accumsan lacus vel facilisis.</div>
  <div class="abs quote-card" style="left:625px">Lorem ipsum dolor sit amet, consectetur adipiscing elit, sed do eiusmod tempor incididunt ut labore et dolore magna aliqua. Quis ipsum suspendisse ultrices gravida. Risus commodo viverra maecenas accumsan lacus vel facilisis.</div>

  <svg class="abs avatar" style="left:196px" width="104" height="118" viewBox="0 0 104 118" role="img" aria-label="Client portrait: veterinarian in blue scrubs with a dog">
    <defs><linearGradient id="av1" x1="0" y1="0" x2="1" y2="1"><stop offset="0" stop-color="#d9cdb4"/><stop offset="1" stop-color="#3f8fd0"/></linearGradient></defs>
    <polygon points="52,2 102,30 102,88 52,116 2,88 2,30" fill="url(#av1)" stroke="#ffffff" stroke-width="2"/>
  </svg>
  <div class="abs client-name" style="left:313px">Elsa Marrow</div>
  <svg class="abs avatar" style="left:630px" width="104" height="118" viewBox="0 0 104 118" role="img" aria-label="Client portrait: veterinarian in blue scrubs holding a kitten">
    <defs><linearGradient id="av2" x1="0" y1="0" x2="1" y2="1"><stop offset="0" stop-color="#e9ece6"/><stop offset="1" stop-color="#4a8cc4"/></linearGradient></defs>
    <polygon points="52,2 102,30 102,88 52,116 2,88 2,30" fill="url(#av2)" stroke="#ffffff" stroke-width="2"/>
  </svg>
  <div class="abs client-name" style="left:757px">Tomas Brill</div>

  <!-- footer -->
  <footer class="abs footer"></footer>
  <svg class="abs cta-shape" width="809" height="168" viewBox="0 0 809 168">
    <polygon points="0,0 809,0 809,89 0,168" fill="#1663c2"/>
  </svg>
  <h2 class="abs cta-title">Lorem Ipsum</h2>
  <p class="abs cta-text">Lorem ipsum dolor sit amet, consectetur adipiscing<br>elit, sed do eiusmod tempor incididunt ut labore</p>
  <div class="abs cta-btn">GET A FREE QUOTE</div>

  <h4 class="abs col-title" style="left:223px">About PawRank</h4>
  <div class="abs col-rule" style="left:223px"></div>
  <p class="abs col-text" style="left:226px;width:175px">Lorem ipsum dolor sit amet, consectetur adipiscing elit, sed do eiusmod tempor incididunt ut labore et dolore magna aliqua. Quis ipsum suspendisse ultrices</p>

  <h4 class="abs col-title" style="left:406px">Categories</h4>
  <div class="abs col-rule" style="left:406px"></div>
  <ul class="abs col-list" style="left:410px;top:2958px">
    <li>Lorem Ipsum</li><li>Lorem Ipsum</li><li>Lorem Ipsum</li><li>Lorem Ipsum</li><li>Lorem Ipsum</li>
  </ul>

  <h4 class="abs col-title" style="left:577px">Our Services</h4>
  <div class="abs col-rule" style="left:577px"></div>
  <ul class="abs col-list" style="left:579px;top:2955px">
    <li>Lorem Ipsum</li><li>Lorem Ipsum</li><li>Lorem Ipsum</li><li>Lorem Ipsum</li><li>Lorem Ipsum</li>
  </ul>

  <h4 class="abs col-title" style="left:761px">Contact Us</h4>
  <div class="abs col-rule" style="left:761px"></div>
  <div class="abs field" style="left:760px;top:2956px;width:105px">First Name</div>
  <div class="abs field" style="left:872px;top:2956px;width:106px">Last Name</div>
  <div class="abs field" style="left:760px;top:2997px;width:218px">E-mail Address</div>
  <div class="abs field send" style="left:760px;top:3041px;width:218px">SEND MESSAGES</div>
</div>
</body>
</html>
```